Brightvale Capital brochure for Investment partnership, young harold pemby

We need a brochure design to attract new investors for our investing partnership Called Brighttvale Capital. We are based in New Orleans, La. We primarily invest in stocks, bonds, and crypto but venture out into other categories as well. We would like to see designs with the black and gold like our logo. The final design should say new, fresh, sleek, tech, and honorable. BROUCHURE WILL BE 4 pages.or one folded sheet a paparer if that makes sense.

A chart showing Brighttvae Capital gains since 2019 28.6 percent and the KT 300 gAINS 7.1 PERCENT

Probable Investors

Financial Planning

• Black and Gold accent. Stock market feel. Sleek, High tech, innovative, Intellgent design.
• Page colors possibly black.
• Boring, Old school,

```html
<!DOCTYPE html>
<html lang="en">
<head>
<meta charset="utf-8">
<title>Brightvale Capital — Brochure</title>
<link rel="stylesheet" href="https://fonts.googleapis.com/css2?family=Crimson+Text:wght@400;600&display=swap">
<style>
  :root {
    --stage: #dcdcdd;
    --ink: #0e0e10;
    --ink-soft: #1d1d21;
    --gold: #e3c326;
    --gold-deep: #b48f12;
    --gold-light: #f6e27a;
    --photo-dark: #2c2c2e;
    --photo-mid: #7a7a7c;
    --photo-light: #c9c9cb;
  }
  * { box-sizing: border-box; margin: 0; padding: 0; }
  html, body { width: 1200px; height: 2497px; overflow: hidden; }
  body {
    background: var(--stage);
    font-family: "Crimson Text", Georgia, serif;
    position: relative;
  }
  .panel { position: absolute; left: 0; width: 1200px; height: 832px; }
  .panel--cover { top: 0; }
  .panel--inside { top: 832px; border-top: 1px solid #d0d0d1; }
  .panel--outside { top: 1664px; border-top: 1px solid #d0d0d1; height: 833px; }

  .cover-scale { position: absolute; left: 350px; top: 62px; width: 400px; height: 566px; transform: scale(1.25); transform-origin: 0 0; }
  .spread { position: absolute; left: 200px; top: 133px; width: 800px; height: 566px; display: flex; box-shadow: 0 18px 40px rgba(0,0,0,.22); }
  .cover-scale .page { box-shadow: 0 14px 32px rgba(0,0,0,.22); }

  .page {
    position: relative; width: 400px; height: 566px; overflow: hidden;
    background: linear-gradient(160deg, var(--ink-soft) 0%, var(--ink) 70%);
    color: var(--gold);
  }
  .page::before, .page::after {
    content: ""; position: absolute; left: 0; right: 0; height: 5px; z-index: 5;
    background: linear-gradient(90deg, var(--gold-deep), var(--gold-light), var(--gold), var(--gold-deep));
  }
  .page::before { top: 0; }
  .page::after { bottom: 0; }
  .spread .page + .page { box-shadow: inset 14px 0 22px -12px rgba(0,0,0,.8); }

  .art { position: absolute; left: 0; top: 0; width: 400px; height: 566px; }

  .brand { position: absolute; text-align: center; color: var(--gold); font-weight: 600; line-height: 1; }
  .brand__name { display: block; letter-spacing: .04em; text-transform: uppercase; }
  .brand__sub { display: block; letter-spacing: .5em; text-transform: uppercase; border-top: 1px solid var(--gold); padding-top: 4px; margin-top: 4px; }

  .cover .brand { left: 90px; top: 300px; width: 260px; }
  .cover .brand__name { font-size: 34px; }
  .cover .brand__sub { font-size: 13px; }
  .tagline {
    position: absolute; left: 44px; top: 372px; width: 320px;
    border-left: 2px solid var(--gold); padding-left: 12px;
    font-size: 16px; line-height: 1.2; color: var(--gold);
  }

  .intro-text {
    position: absolute; left: 34px; top: 44px; width: 280px;
    font-size: 15.5px; line-height: 1.35; font-style: italic; color: var(--gold);
  }
  .inside-left .brand { right: 22px; top: 46px; width: 80px; }
  .inside-left .brand__name, .outside-back .brand__name { font-size: 13px; }
  .inside-left .brand__sub, .outside-back .brand__sub { font-size: 6px; letter-spacing: .4em; }

  .how { position: absolute; left: 30px; top: 40px; width: 340px; text-align: center; }
  .how__title { font-size: 20px; font-weight: 600; text-decoration: underline; text-underline-offset: 3px; margin-bottom: 14px; text-align: right; padding-right: 20px; }
  .step { margin-bottom: 16px; }
  .step__icon { display: block; margin: 0 auto 8px; }
  .step__text { font-size: 11.5px; line-height: 1.35; }

  .about { position: absolute; left: 22px; top: 318px; width: 300px; }
  .about__title { font-size: 15px; font-weight: 600; border-bottom: 1px solid var(--gold); padding-bottom: 6px; margin-bottom: 8px; }
  .about__body { font-size: 9.5px; line-height: 1.4; }
  .outside-back .brand { right: 26px; top: 270px; width: 90px; }
</style>
</head>
<body>

<section class="panel panel--cover">
  <div class="cover-scale">
    <article class="page cover">
      <svg class="art" viewBox="0 0 400 566" aria-hidden="false">
        <defs>
          <linearGradient id="coverPhoto" x1="0" y1="0" x2="1" y2="1">
            <stop offset="0" stop-color="var(--photo-light)"/>
            <stop offset=".5" stop-color="var(--photo-mid)"/>
            <stop offset="1" stop-color="var(--photo-dark)"/>
          </linearGradient>
        </defs>
        <polygon role="img" aria-label="Black and white photograph of a historic cathedral and balconied French Quarter street" points="120,0 400,0 400,300" fill="url(#coverPhoto)"/>
        <line x1="120" y1="0" x2="400" y2="300" stroke="var(--gold)" stroke-width="3"/>
      </svg>
      <div class="brand"><span class="brand__name">Brightvale</span><span class="brand__sub">Capital</span></div>
      <p class="tagline">Become a partner and build generational wealth by investing in the stock market<br>A first of its kind Investment Club</p>
    </article>
  </div>
</section>

<section class="panel panel--inside">
  <div class="spread">
    <article class="page inside-left">
      <svg class="art" viewBox="0 0 400 566">
        <defs>
          <linearGradient id="handshakePhoto" x1="0" y1="0" x2="1" y2="1">
            <stop offset="0" stop-color="var(--photo-mid)"/>
            <stop offset=".6" stop-color="var(--photo-light)"/>
            <stop offset="1" stop-color="var(--photo-dark)"/>
          </linearGradient>
        </defs>
        <path role="img" aria-label="Black and white photograph of a business handshake over stock market chart overlays" d="M0,330 Q230,250 300,566 L0,566 Z" fill="url(#handshakePhoto)"/>
        <path d="M0,330 Q230,250 300,566" fill="none" stroke="var(--gold)" stroke-width="3"/>
      </svg>
      <div class="brand"><span class="brand__name">Brightvale</span><span class="brand__sub">Capital</span></div>
      <p class="intro-text">If you are receiving this brochure its because someone sees you as a person that doesn't want to just work and pay bills. Your someone who wants to build real generational wealth. Not throw schemes but the using the greatest wealth builder available. The stock market.</p>
    </article>

    <article class="page inside-right">
      <div class="how">
        <h2 class="how__title">How it works</h2>
        <div class="step">
          <svg class="step__icon" width="40" height="40" viewBox="0 0 40 40" aria-hidden="true">
            <circle cx="20" cy="20" r="18" fill="none" stroke="var(--gold)" stroke-width="2"/>
            <path d="M11 17 L20 11 L29 17 Z M12 28 H28 M14 19 V26 M18 19 V26 M22 19 V26 M26 19 V26" fill="var(--gold)" stroke="var(--gold)" stroke-width="2"/>
          </svg>
          <p class="step__text">Make initial deposit. The general partner will invest in stocks, bonds and other investment vehicles on your behalf.</p>
        </div>
        <div class="step">
          <svg class="step__icon" width="40" height="40" viewBox="0 0 40 40" aria-hidden="true">
            <circle cx="20" cy="20" r="18" fill="none" stroke="var(--gold)" stroke-width="2"/>
            <path d="M16 12 H24 L22 15 C29 18 29 29 20 29 C11 29 11 18 18 15 Z" fill="var(--gold)"/>
            <text x="20" y="26" text-anchor="middle" font-size="10" fill="var(--ink)" font-family="Crimson Text, serif">$</text>
          </svg>
          <p class="step__text">There is no upfront fees. The general plpartner will guarantee a 5 percent return and will work for free on your behalf until that is achieved. After the 5 percent return on the dollars invested the limited partner will receive 80 percent and the general partner will receive 20 percent of every dollar gained</p>
        </div>
        <div class="step">
          <svg class="step__icon" width="40" height="40" viewBox="0 0 40 40" aria-hidden="true">
            <circle cx="20" cy="20" r="18" fill="none" stroke="var(--gold)" stroke-width="2"/>
            <circle cx="22" cy="15" r="5" fill="var(--gold)"/>
            <path d="M9 25 H16 L22 22 C25 21 27 23 24 25 L18 28 H9 Z" fill="var(--gold)"/>
          </svg>
          <p class="step__text">As the return and investments multiply the interests begins to compound annually. The legal partner legally owns shares of stock within the club and may redeem once a year or let money continue to earn interest.</p>
        </div>
      </div>
    </article>
  </div>
</section>

<section class="panel panel--outside">
  <div class="spread">
    <article class="page outside-back">
      <svg class="art" viewBox="0 0 400 566">
        <defs>
          <linearGradient id="streetPhoto" x1="0" y1="0" x2="1" y2="1">
            <stop offset="0" stop-color="var(--photo-dark)"/>
            <stop offset=".55" stop-color="var(--photo-mid)"/>
            <stop offset="1" stop-color="var(--photo-light)"/>
          </linearGradient>
        </defs>
        <path role="img" aria-label="Black and white photograph of a historic city street with a horse carriage and a statue" d="M0,0 H400 V250 Q200,150 0,240 Z" fill="url(#streetPhoto)"/>
        <path d="M0,240 Q200,150 400,250" fill="none" stroke="var(--gold)" stroke-width="3"/>
      </svg>
      <div class="brand"><span class="brand__name">Brightvale</span><span class="brand__sub">Capital</span></div>
      <div class="about">
        <h2 class="about__title">About Brightvale Capital and General Partner</h2>
        <p class="about__body">Brightvale Capital was founded in 2019 by General Partner Marcus Ellery with a group economic empowerment mission. Marcus Ellery has invested in stocks since a teenager, received his BA in economics from Bayou Crescent University and is currently attending The university of Gulf Plains.</p>
      </div>
    </article>

    <article class="page cover">
      <svg class="art" viewBox="0 0 400 566">
        <defs>
          <linearGradient id="coverPhotoBack" x1="0" y1="0" x2="1" y2="1">
            <stop offset="0" stop-color="var(--photo-light)"/>
            <stop offset=".5" stop-color="var(--photo-mid)"/>
            <stop offset="1" stop-color="var(--photo-dark)"/>
          </linearGradient>
        </defs>
        <polygon role="img" aria-label="Black and white photograph of a historic cathedral and balconied French Quarter street" points="120,0 400,0 400,300" fill="url(#coverPhotoBack)"/>
        <line x1="120" y1="0" x2="400" y2="300" stroke="var(--gold)" stroke-width="3"/>
      </svg>
      <div class="brand"><span class="brand__name">Brightvale</span><span class="brand__sub">Capital</span></div>
      <p class="tagline">Become a partner and build generational wealth by investing in the stock market<br>A first of its kind Investment Club</p>
    </article>
  </div>
</section>

</body>
</html>
```